Creation of an elegant and modern turnkey Shopify website

Hello,

We are a new company specializing in the sale of above-ground pools. We want to create a turnkey website, ideally using Shopify. For now, we need a "showcase" site, not an e-commerce platform, with four tabs:

Home Page (an overall presentation of the company)
Our Products (an overview of all the above-ground pools we sell)
Our Projects (a page inspired by Instagram to showcase photos of our future projects)
Contact (a page with all our contact information and a contact form)

We are looking to create a highly visual, elegant, and modern website with vibrant splashes of color. We will provide the text, photos (along with instructions on where to place them on each page), and all other necessary information as attachments.

Thank you in advance for your proposals!

The Brisa Lagoon Team

Target Market(s)

Targeted at Swiss customers (a translator will need to be installed for different languages)

Industry/Entity Type

Sale of customised above-ground pools

Coding

Coded - Design and coding required

Font styles to use
Sans Serif

Colors
0094D4
00A9DD
6FCCEA
C7EBF8
E9F6FB
00AB8E
00BBA5
67D7C9
C6EFE9
E9F9F6

Requirements
Must have
• A stunning, elegant and modern look
Nice to have
• Inspiration from the colors of our logo throughout the site, but in an elegant way
Should not have
• An overly classic look for swimming pool sites

```html
<!DOCTYPE html>
<html lang="en">
<head>
<meta charset="utf-8">
<title>Brisa Lagoon – Above-Ground Pools</title>
<link href="https://fonts.googleapis.com/css2?family=Didact+Gothic&family=Roboto:wght@400;500;700&display=swap" rel="stylesheet">
<style>
:root{
  --page-bg:#eef1f3;
  --white:#ffffff;
  --brand-blue:#00A9DD;
  --deep-blue:#0094D4;
  --sky:#6FCCEA;
  --ice:#E9F6FB;
  --slate:#585858;
  --slate-dark:#4a4a4a;
  --ink:#3d3d3d;
  --muted:#6d7a80;
  --cyan-head:#2fd0f0;
  --pale-cyan:#7fe0f5;
}
*{box-sizing:border-box;margin:0;padding:0}
html,body{width:1200px;height:2867px;overflow:hidden}
body{background:var(--page-bg);font-family:"Roboto",sans-serif;color:var(--ink);position:relative}
.page{position:absolute;left:0;top:147px;width:1200px;height:2572px;background:var(--white);box-shadow:0 4px 24px rgba(0,0,0,.08)}
.abs{position:absolute}
.head-font{font-family:"Didact Gothic",sans-serif;font-weight:400}

/* header */
.site-header{left:0;top:0;width:1200px;height:56px;background:var(--white)}
.brand-box{left:170px;top:11px;width:107px;height:83px;background:var(--white);z-index:3;display:flex;flex-direction:column;align-items:center;justify-content:center;box-shadow:0 1px 3px rgba(0,0,0,.08)}
.brand-name{font-family:"Didact Gothic",sans-serif;color:var(--brand-blue);font-size:21px;line-height:1.05;text-align:center;letter-spacing:1px}
.main-nav a{position:absolute;top:21px;font-size:11px;color:var(--ink);text-decoration:none}
.main-nav a.active{color:var(--brand-blue);text-decoration:underline;text-underline-offset:3px}
.lang-select{left:854px;top:16px;width:51px;height:24px;border:1px solid #dde3e6;border-radius:12px;font-size:10px;display:flex;align-items:center;padding-left:11px;gap:9px}
.lang-select::after{content:"";border:3px solid transparent;border-top-color:var(--ink);margin-top:3px}
.call-icon{left:923px;top:14px;width:27px;height:27px;border-radius:50%;background:var(--brand-blue);display:flex;align-items:center;justify-content:center}
.call-text{left:958px;top:15px;line-height:1.1}
.call-text small{display:block;font-size:8.5px;color:var(--muted)}
.call-text strong{font-size:11.5px;font-weight:700}

/* hero */
.hero-photo{left:0;top:56px;width:1200px;height:488px;background:linear-gradient(160deg,#6b7f4a 0%,#c9a97a 28%,#2fb3d9 55%,#1f8fbf 72%,#3c6e2e 100%)}
.hero-card{left:775px;top:144px;width:268px;height:313px;background:rgba(40,40,40,.72);padding:28px 0 0 37px;color:var(--white)}
.hero-title{font-size:39px;line-height:41px;letter-spacing:1px}
.btn-more{display:inline-block;margin-top:20px;background:var(--white);color:var(--ink);font-size:11px;padding:9px 19px}
.slider-dots{display:flex;gap:9px;margin-top:17px}
.slider-dots span{width:13px;height:13px;border:1.3px solid #cfcfcf;border-radius:50%;display:flex;align-items:center;justify-content:center}
.slider-dots span.on::after{content:"";width:5px;height:5px;border-radius:50%;background:var(--sky)}

/* feature rows */
.photo{position:absolute}
.panel{position:absolute;padding:0 30px}
.panel-blue{background:var(--brand-blue);color:var(--white)}
.panel-slate{background:var(--slate);color:var(--white)}
.panel h2{font-family:"Didact Gothic",sans-serif;font-weight:400;font-size:22px;line-height:25px;letter-spacing:.5px}
.panel p{font-size:10.5px;line-height:13px;text-transform:capitalize;margin-top:13px}
.panel-slate h2{color:var(--cyan-head)}
.title-pale{color:var(--pale-cyan)}
.warranty{font-family:"Didact Gothic",sans-serif;color:var(--pale-cyan);font-size:17px;margin-top:18px}

/* why choose */
.why-title{left:0;top:950px;width:1200px;text-align:center;font-size:21px;color:var(--ink)}
.why-cards{left:156px;top:990px;width:887px;height:182px;display:flex;gap:5px}
.why-card{flex:1;background:var(--ice);padding:16px 12px 0 13px}
.why-card svg{display:block;height:34px}
.why-card h3{font-family:"Didact Gothic",sans-serif;font-weight:400;font-size:13px;margin-top:17px;color:var(--ink)}
.why-card p{font-size:9.5px;line-height:11.5px;color:var(--muted);margin-top:13px;text-transform:capitalize}

/* footer */
.site-footer{left:0;top:2321px;width:1200px;height:215px;background:var(--deep-blue);color:var(--white)}
.footer-brand{left:156px;top:60px;font-family:"Didact Gothic",sans-serif;color:var(--cyan-head);font-size:38px;line-height:42px;letter-spacing:1px}
.footer-col{top:44px}
.footer-col h4{font-size:12.5px;font-weight:700;margin-bottom:15px}
.footer-col li{list-style:none;font-size:10.5px;line-height:13px;margin-bottom:10px;display:flex;gap:6px}
.footer-col a{color:var(--white);text-decoration:none}
.footer-col a.active{color:var(--pale-cyan);text-decoration:underline}
.footer-map{left:755px;top:45px;width:288px;height:124px;background:linear-gradient(135deg,#eef0f2,#dfe4e8)}
.bottom-bar{left:0;top:2536px;width:1200px;height:36px;background:var(--slate-dark);color:var(--white);font-size:10px}
.copyright{left:156px;top:12px}
.social{left:970px;top:8px;display:flex;gap:8px}
.social span{width:20px;height:20px;border-radius:50%;background:var(--brand-blue)}
.social span:first-child{background:var(--cyan-head)}
</style>
</head>
<body>
<div class="page">

  <header class="site-header abs">
    <div class="brand-box abs"><span class="brand-name">BRISA<br>LAGOON</span></div>
    <nav class="main-nav">
      <a class="active" style="left:488px" href="#">Home</a>
      <a style="left:552px" href="#">Our Products</a>
      <a style="left:653px" href="#">Our Projects</a>
      <a style="left:751px" href="#">Contact Us</a>
    </nav>
    <div class="lang-select abs">En</div>
    <div class="call-icon abs">
      <svg width="13" height="13" viewBox="0 0 24 24"><path fill="#fff" d="M6.6 10.8a15.1 15.1 0 0 0 6.6 6.6l2.2-2.2a1 1 0 0 1 1-.25 11.4 11.4 0 0 0 3.6.57 1 1 0 0 1 1 1V20a1 1 0 0 1-1 1A17 17 0 0 1 3 4a1 1 0 0 1 1-1h3.5a1 1 0 0 1 1 1c0 1.25.2 2.45.57 3.57a1 1 0 0 1-.25 1z"/></svg>
    </div>
    <div class="call-text abs"><small>Call Now</small><strong>079 555 21 30</strong></div>
  </header>

  <section class="hero">
    <div class="hero-photo abs" role="img" aria-label="Modern villa with long turquoise pool, wooden deck and white loungers"></div>
    <div class="hero-card abs">
      <h1 class="hero-title head-font">Build Your Dream Swimming Pool</h1>
      <span class="btn-more">More Info</span>
      <div class="slider-dots"><span></span><span class="on"></span><span></span></div>
    </div>
  </section>

  <section class="feature-intro">
    <div class="photo" style="left:156px;top:550px;width:588px;height:363px;background:linear-gradient(150deg,#2f5a2a,#3fb3c9 55%,#8a6a48)" role="img" aria-label="Curved lagoon pool with rock edges, wooden deck and outdoor lounge"></div>
    <div class="panel panel-blue" style="left:750px;top:550px;width:293px;height:363px;padding-top:54px">
      <h2>Transform Your Garden With Our Premium Above-Ground Pools!</h2>
      <p style="margin-top:18px">Achieve your dreams with our custom, tailor-made above-ground pools.</p>
      <p>Imagine an exceptional relaxation and leisure space right in your own backyard. With our unparalleled expertise and commitment to excellence, we create above-ground pools that exceed all expectations. Our exclusive, custom-designed models are crafted to combine style, durability, and innovation, offering a unique and refined experience.</p>
    </div>
  </section>

  <section class="why-choose">
    <h2 class="why-title abs head-font">Why Choose Our Above-Ground Pools?</h2>
    <div class="why-cards abs">
      <div class="why-card">
        <svg viewBox="0 0 34 34" width="34"><path d="M7 10h20l5 7-15 15L2 17z M2 17h30 M12 10l5 22 5-22" fill="none" stroke="#00A9DD" stroke-width="1.3"/></svg>
        <h3>Superior Quality:</h3>
        <p>Each pool is constructed with high-quality materials, ensuring exceptional durability and strength.</p>
      </div>
      <div class="why-card">
        <svg viewBox="0 0 34 34" width="34"><path d="M4 30l14-14 M18 16l3 3 M24 4v6 M21 7h6 M29 14v4 M27 16h4 M12 6v4 M10 8h4" fill="none" stroke="#00A9DD" stroke-width="1.3"/></svg>
        <h3>Elegant Design:</h3>
        <p>Our pools come in a variety of styles and finishes, seamlessly blending into any garden setting.</p>
      </div>
      <div class="why-card">
        <svg viewBox="0 0 34 34" width="34"><path d="M3 6h18 M3 6v25h25V14 M10 24l3-8 15-14 5 5-15 15z" fill="none" stroke="#00A9DD" stroke-width="1.3"/></svg>
        <h3>Custom &amp; Tailor-Made:</h3>
        <p>Create the pool of your dreams with our customization options, tailored to your specific tastes and needs.</p>
      </div>
      <div class="why-card">
        <svg viewBox="0 0 34 34" width="34"><circle cx="17" cy="17" r="6" fill="none" stroke="#00A9DD" stroke-width="1.3"/><circle cx="17" cy="17" r="13" fill="none" stroke="#00A9DD" stroke-width="1.3" stroke-dasharray="5 3"/></svg>
        <h3>Easy Installation:</h3>
        <p>Enjoy your new oasis quickly with our simple and fast installation process.</p>
      </div>
      <div class="why-card">
        <svg viewBox="0 0 34 34" width="34"><path d="M17 6a8 8 0 0 0-5 14v4h10v-4a8 8 0 0 0-5-14z M13 28h8 M17 1v2 M5 12h2 M27 12h2 M8 4l2 2 M26 4l-2 2" fill="none" stroke="#00A9DD" stroke-width="1.3"/></svg>
        <h3>Constant Innovation:</h3>
        <p>We incorporate the latest technologies to provide you with an optimal and safe swimming experience.</p>
      </div>
    </div>
  </section>

  <section class="feature-services">
    <div class="panel panel-slate" style="left:156px;top:1215px;width:294px;height:362px;padding-top:88px">
      <h2>Personalized<br>Services</h2>
      <p style="margin-top:28px">We understand that every garden and client is unique.</p>
      <p>That's why we offer personalized services, from design to installation and after-sales support.</p>
      <p>Our team of experts is here to answer all your questions and guide you throughout your project.</p>
    </div>
    <div class="photo" style="left:456px;top:1215px;width:587px;height:362px;background:linear-gradient(180deg,#5fd0e6,#a9dfe6 45%,#d8cbb4)" role="img" aria-label="Pool cleaning kit with hose, brush, net and water test bottles by the poolside"></div>
  </section>

  <section class="feature-satisfaction">
    <div class="photo" style="left:156px;top:1583px;width:588px;height:361px;background:linear-gradient(150deg,#3f7a3a,#28a9d6 50%,#8b7a64)" role="img" aria-label="Tiled pool with steel ladder beside a garden of palms"></div>
    <div class="panel panel-blue" style="left:750px;top:1583px;width:293px;height:361px;padding-top:76px">
      <h2 class="title-pale">Guaranteed<br>Satisfaction</h2>
      <p style="margin-top:22px">Your satisfaction is our top priority.</p>
      <p>We are committed to providing you with exceptional service and the highest quality products.</p>
      <p>Join our community of satisfied customers who are already enjoying their custom above-ground pools.</p>
      <div class="warranty">10-Year Warranty!</div>
    </div>
  </section>

  <section class="feature-contact">
    <div class="panel panel-slate" style="left:156px;top:1952px;width:294px;height:361px;padding-top:94px">
      <h2>Contact Us<br>Today</h2>
      <p style="margin-top:28px">Don't wait any longer to transform your garden into a wellness oasis.</p>
      <p>Contact us today to discover our range of customizable above-ground pools and get a tailored quote.</p>
      <p>Dive into a world of infinite possibilities with [your company name].</p>
    </div>
    <div class="photo" style="left:456px;top:1952px;width:587px;height:361px;background:linear-gradient(160deg,#37b9e6,#8fd6ee 45%,#e7e2dc 70%,#8a5a3c)" role="img" aria-label="Woman relaxing on a pool deck while using a phone"></div>
  </section>

  <footer class="site-footer abs">
    <div class="footer-brand abs">BRISA<br>LAGOON</div>
    <div class="footer-col abs" style="left:373px">
      <h4>Contact Us</h4>
      <ul>
        <li><svg width="10" height="10" viewBox="0 0 24 24"><path fill="#7fe0f5" d="M6.6 10.8a15.1 15.1 0 0 0 6.6 6.6l2.2-2.2a1 1 0 0 1 1-.25 11.4 11.4 0 0 0 3.6.57 1 1 0 0 1 1 1V20a1 1 0 0 1-1 1A17 17 0 0 1 3 4a1 1 0 0 1 1-1h3.5a1 1 0 0 1 1 1c0 1.25.2 2.45.57 3.57a1 1 0 0 1-.25 1z"/></svg>079 555 21 30</li>
        <li><svg width="10" height="10" viewBox="0 0 24 24"><path fill="#7fe0f5" d="M2 5h20v14H2z"/><path d="M2 5l10 8 10-8" fill="none" stroke="#0094D4" stroke-width="2"/></svg>info@brisalagoon.ch</li>
        <li><svg width="10" height="12" viewBox="0 0 24 28"><path fill="#7fe0f5" d="M12 0a9 9 0 0 0-9 9c0 7 9 19 9 19s9-12 9-19a9 9 0 0 0-9-9zm0 12a3 3 0 1 1 0-6 3 3 0 0 1 0 6z"/></svg><span>Marco Vellini<br>Chemin des Saules 28<br>1870 Monthey</span></li>
      </ul>
    </div>
    <div class="footer-col abs" style="left:593px">
      <h4>Quick Links</h4>
      <ul>
        <li><a class="active" href="#">Home</a></li>
        <li><a href="#">Our Products</a></li>
        <li><a href="#">Our Projects</a></li>
        <li><a href="#">Contact Us</a></li>
      </ul>
    </div>
    <div class="footer-map abs" role="img" aria-label="Street map showing the showroom location"></div>
  </footer>

  <div class="bottom-bar abs">
    <span class="copyright abs">© 2024 The Brisa Lagoon Team. All Right Reserved</span>
    <div class="social abs"><span></span><span></span><span></span></div>
  </div>

</div>
</body>
</html>
```